SKYVANTEX (drone photo and video) and Photogrammetry Services (mapping and 3D modeling)

We need a business card design for a SKYVANTEX. Our businesses provides (drone) Aerial Photo and Video Captures. However we also provide Photogrammetry (which is 3D modeling and mapping). We greatly value unique points of view taken of landscapes and subjects with aerial photography and videography. 3D modeling and mapping is the other area of focus and have an incredibly broad scope of applications and imaginative creativity.

Target Market(s)

Based out of Northern Virginia and serving the greater Virginia and Maryland areas

Industry/Entity Type

Drone Photo and video and Photogrammetry Services (mapping and 3D modeling)

Contact Information for Business Card

3D Models, Maps and Photo/Video Production name: Marcus Pettibone email: mqp@skyvantex.us website: skyvantex.us phone: 571-806-3394; please also include "Aerial Photo/Video and 3D Mapping/Modeling"

Requirements
Must have
• Please make this design vertical and double sided. The selection box is not letting me choose Double Sided but that is my wish. Incorporate uploaded LOGO and color scheme
Nice to have
• Preferably does not feel too crowded and balances not having an exaggerated amount of distracting detail
Should not have
• do not cram bullet points or text in long form

```html
<!DOCTYPE html>
<html lang="en">
<head>
<meta charset="utf-8">
<title>SKYVANTEX Business Card</title>
<link rel="stylesheet" href="https://fonts.googleapis.com/css2?family=Montserrat:wght@800&family=Roboto+Condensed:wght@400;700&display=swap">
<style>
  :root {
    --backdrop: #2a2b2e;
    --navy: #2b3a46;
    --navy-deep: #1c2731;
    --paper: #ffffff;
    --paper-shade: #eceeef;
    --ink: #23272b;
    --sun-yellow: #f5c33a;
    --sun-orange: #f27a34;
    --sun-red: #ee3b3f;
  }
  * { box-sizing: border-box; margin: 0; padding: 0; }
  html, body {
    width: 1200px; height: 960px; overflow: hidden;
    background: var(--backdrop);
  }
  .sheet {
    position: relative; width: 1200px; height: 960px;
    display: flex; justify-content: center; align-items: center; gap: 100px;
  }
  .card {
    position: relative; width: 380px; height: 665px; overflow: hidden;
    box-shadow: 0 18px 40px rgba(0,0,0,.45);
  }
  /* Front */
  .card--front {
    background: linear-gradient(160deg, var(--navy) 0%, var(--navy-deep) 100%);
  }
  .front-panel {
    position: absolute; left: 88px; top: 0; width: 216px; height: 350px;
    background: linear-gradient(180deg, var(--paper-shade), var(--paper));
  }
  .mark-ring {
    position: absolute; left: 130px; top: 196px; width: 196px; height: 196px;
    border-radius: 50%; background: var(--navy);
  }
  .mark-disc {
    position: absolute; left: 150px; top: 216px; width: 156px; height: 156px;
    border-radius: 50%;
    background: linear-gradient(45deg, var(--sun-yellow), var(--sun-orange) 55%, var(--sun-red));
  }
  .brand-name {
    position: absolute; left: 0; width: 100%; text-align: center;
    font-family: "Montserrat", sans-serif; font-weight: 800;
    letter-spacing: 2px;
  }
  .card--front .brand-name { top: 404px; font-size: 38px; color: var(--paper); }
  .front-rule {
    position: absolute; left: 70px; right: 26px; top: 590px; height: 1px;
    background: linear-gradient(90deg, var(--sun-yellow), var(--sun-red));
    opacity: .7;
  }
  /* Back */
  .card--back { background: linear-gradient(170deg, #f3f4f5 0%, var(--paper) 40%); }
  .card--back .mark-disc { left: 120px; top: 70px; width: 140px; height: 140px; }
  .card--back .brand-name { top: 226px; font-size: 34px; color: var(--ink); }
  .contact {
    position: absolute; left: 96px; top: 430px;
    font-family: "Roboto Condensed", sans-serif; color: var(--ink);
  }
  .contact__name { font-weight: 700; font-size: 19px; letter-spacing: .5px; margin-bottom: 8px; }
  .contact__line { display: flex; align-items: center; gap: 8px; font-size: 16px; line-height: 22px; }
  .contact__line svg { width: 11px; height: 11px; flex: none; }
  .back-rule {
    position: absolute; left: 24px; right: 24px; top: 580px; height: 2px;
    background: linear-gradient(90deg, var(--sun-yellow), var(--sun-red));
  }
  .tagline {
    position: absolute; left: 0; width: 100%; top: 606px; text-align: center;
    font-family: "Roboto Condensed", sans-serif; font-weight: 700;
    font-size: 18px; color: var(--ink);
  }
</style>
</head>
<body>
<main class="sheet">
  <section class="card card--front" aria-label="Card front">
    <div class="front-panel"></div>
    <div class="mark-ring"></div>
    <div class="mark-disc"></div>
    <p class="brand-name">SKYVANTEX</p>
    <div class="front-rule"></div>
  </section>

  <section class="card card--back" aria-label="Card back">
    <div class="mark-disc"></div>
    <p class="brand-name">SKYVANTEX</p>
    <div class="contact">
      <p class="contact__name">MARCUS PETTIBONE</p>
      <p class="contact__line">
        <svg viewBox="0 0 12 12"><path d="M3 1l2 2.5-1.2 1.2c.6 1.4 1.8 2.6 3.2 3.2L8.2 6.7 11 8.7 9.8 11C5 10.6 1.4 7 1 2.2z" fill="#23272b"/></svg>
        571-806-3394
      </p>
      <p class="contact__line">
        <svg viewBox="0 0 12 12"><rect x="1" y="2.5" width="10" height="7" fill="#23272b"/><path d="M1 2.5l5 4 5-4" stroke="#fff" fill="none"/></svg>
        mqp@skyvantex.us
      </p>
      <p class="contact__line">
        <svg viewBox="0 0 12 12"><circle cx="6" cy="6" r="5" fill="none" stroke="#23272b" stroke-width="1.4"/><path d="M1 6h10M6 1c-2.5 3-2.5 7 0 10M6 1c2.5 3 2.5 7 0 10" stroke="#23272b" fill="none"/></svg>
        www.skyvantex.us
      </p>
    </div>
    <div class="back-rule"></div>
    <p class="tagline">Aerial Photo/Video and 3D Mapping/Modeling</p>
  </section>
</main>
</body>
</html>
```